Business Card Design with existing logo

AmberOwl provides inspirational leadership training and coaching for corporate executives. We focus on being challenging, humorous and compassionate, providing the right mix of support and push for individuals and teams to improve their knowledge and performance. The colour purple is essential to the design. We already have a logo we are very happy with - we are curious to see what can be done to come across in a professional, high standard way that sets us apart. Ideally the design should include the photo of Brigitte
Target Market(s)
HR/ Senior Management 500 - 1500 employees
Industry/Entity Type
Leadership
Contact Information for Business Card
AmberOwl Coaching Ltd
Inspirational leadership
Brigitte Holmqvist Dunmore
Leadership coach and trainer
Telephone: +44 1632 960 418
Mobile: +44 7700 900 562
e-mail: brigitte@amberowlmentoring.example
www.amberowlmentoring.example
Requirements
Must have
- The existing logo
Picture of Brigitte

```html
<!DOCTYPE html>
<html lang="en">
<head>
<meta charset="utf-8">
<title>AmberOwl Coaching – Business Card</title>
<link href="https://fonts.googleapis.com/css2?family=Open+Sans:wght@400;600&display=swap" rel="stylesheet">
<style>
  :root {
    --bg: #d6d6d6;
    --ink: #1c1b1e;
    --purple: #6b3f98;
    --white: #ffffff;
    --text: #1a1a1a;
    --muted: #8a8a8a;
  }
  * { margin: 0; padding: 0; box-sizing: border-box; }
  html, body { width: 1200px; height: 985px; overflow: hidden; }
  body {
    background: var(--bg);
    font-family: "Open Sans", Arial, sans-serif;
    position: relative;
  }
  .card {
    position: absolute;
    left: 320px;
    width: 560px;
    height: 320px;
    border-radius: 22px;
    overflow: hidden;
  }
  /* Front */
  .card--front { top: 120px; background: var(--ink); }
  .front__disc {
    position: absolute; left: 60px; top: 12px;
    width: 250px; height: 250px; border-radius: 50%;
    background: var(--purple);
  }
  .brand {
    position: absolute;
    font-weight: 600;
    letter-spacing: 3px;
    text-transform: uppercase;
    white-space: nowrap;
  }
  .front__brand { left: 200px; top: 228px; font-size: 26px; color: var(--white); }
  .tagline {
    position: absolute;
    font-size: 9px;
    letter-spacing: 4px;
    text-transform: uppercase;
    white-space: nowrap;
    color: var(--muted);
  }
  .front__tagline { left: 262px; top: 266px; }

  /* Back */
  .card--back { top: 500px; background: var(--white); }
  .back__band {
    position: absolute; left: 0; top: 0; width: 100%; height: 100%;
  }
  .back__disc {
    position: absolute; left: 112px; top: 20px;
    width: 76px; height: 76px; border-radius: 50%;
    background: var(--purple);
    border: 3px solid var(--white);
  }
  .back__brand { left: 196px; top: 52px; font-size: 20px; color: var(--purple); }
  .back__tagline { left: 244px; top: 82px; font-size: 7px; }
  .person { position: absolute; left: 150px; top: 112px; }
  .person__name { font-size: 20px; color: var(--text); line-height: 1.2; }
  .person__role { font-size: 14px; color: var(--purple); line-height: 1.35; }
  .person__company, .person__slogan { font-size: 14px; color: var(--text); line-height: 1.3; }
  .role-rule {
    position: absolute; left: 330px; top: 157px;
    width: 200px; height: 1px; background: var(--purple);
  }
  .contact {
    position: absolute; left: 150px; top: 214px;
    list-style: none; font-size: 14px; line-height: 1.3; color: var(--text);
  }
  .contact__web { color: var(--purple); }
  .contact__web span { color: var(--text); }
  .icons {
    position: absolute; left: 72px; top: 212px;
    display: flex; flex-direction: column; gap: 7px;
  }
  .icon {
    width: 12px; height: 12px; border-radius: 2px;
    background: var(--purple);
    display: flex; align-items: center; justify-content: center;
  }
  .icon svg { width: 8px; height: 8px; }
</style>
</head>
<body>

<section class="card card--front" aria-label="Business card front">
  <div class="front__disc"></div>
  <div class="brand front__brand">AmberOwl Coaching</div>
  <div class="tagline front__tagline">Inspirational Leadership</div>
</section>

<section class="card card--back" aria-label="Business card back">
  <svg class="back__band" viewBox="0 0 560 320" preserveAspectRatio="none" aria-hidden="true">
    <polygon points="0,0 150,0 50,320 0,320" fill="#1c1b1e"/>
    <polygon points="150,0 158,0 58,320 50,320" fill="#ffffff"/>
    <polygon points="158,0 162,0 62,320 58,320" fill="#1c1b1e"/>
  </svg>
  <div class="back__disc"></div>
  <div class="brand back__brand">AmberOwl Coaching</div>
  <div class="tagline back__tagline">Inspirational Leadership</div>

  <div class="person">
    <div class="person__name">Brigitte Holmqvist Dunmore</div>
    <div class="person__role">Leadership coach and trainer</div>
    <div class="person__company">AmberOwl Coaching Ltd</div>
    <div class="person__slogan">Inspirational leadership</div>
  </div>
  <div class="role-rule"></div>

  <div class="icons" aria-hidden="true">
    <div class="icon">
      <svg viewBox="0 0 10 10"><path d="M2 1h2l1 2-1 1c.5 1 1 1.5 2 2l1-1 2 1v2c-4 1-8-3-7-7z" fill="#fff"/></svg>
    </div>
    <div class="icon">
      <svg viewBox="0 0 10 10"><circle cx="5" cy="5" r="3.6" fill="none" stroke="#fff" stroke-width="1.2"/><circle cx="5" cy="5" r="1.4" fill="#fff"/></svg>
    </div>
    <div class="icon">
      <svg viewBox="0 0 10 10"><rect x="1" y="2.5" width="8" height="5" fill="none" stroke="#fff" stroke-width="1"/><path d="M1 2.5l4 3 4-3" fill="none" stroke="#fff" stroke-width="1"/></svg>
    </div>
  </div>

  <ul class="contact">
    <li>+44 1632 960 418</li>
    <li>+44 7700 900 562 (Mobile)</li>
    <li>brigitte@amberowlmentoring.example</li>
    <li><span>www.</span><span class="contact__web">amberowlmentoring</span><span>.example</span></li>
  </ul>
</section>

</body>
</html>
```